Trendy, rustic, patriotic Facebook Design!

Would like something to catch people's eye! Must include our logo and phone number. 318-557-0249. Dogs in the project are a must. Bold pricing, location, etc to catch peoples eyes is a plus.

Target Market(s)

Dog owners

Font styles to use
Serif
Sans Serif

Colors
1f66ae
ec1f27
ffffff

Requirements
Must have
• Dogs, company logo, business phone 318-557-0249 and website www.bramblehound.example
Nice to have
• Something that is rustic, trendy!
Should not have
• Cartoons.

```html
<!DOCTYPE html>
<html lang="en">
<head>
<meta charset="utf-8">
<title>Bramblehound Dog Training – Cover Banners</title>
<link rel="stylesheet" href="https://fonts.googleapis.com/css2?family=Montserrat:wght@400;500;800&display=swap">
<style>
  :root {
    --page: #f6f7fa;
    --brand-blue: #1f66ae;
    --brand-navy: #0a2d6b;
    --brand-red: #ec1f27;
    --white: #ffffff;
  }
  html, body {
    margin: 0;
    padding: 0;
    width: 735px;
    height: 1200px;
    overflow: hidden;
    background: var(--page);
    font-family: "Montserrat", sans-serif;
  }
  .sheet {
    position: relative;
    width: 735px;
    height: 1200px;
  }
  .cover {
    position: absolute;
    display: block;
  }
  .cover--classic { --panel: var(--brand-blue); --band: var(--brand-blue); --ring: transparent; }
  .cover--navy    { --panel: var(--brand-navy); --band: var(--brand-blue); --ring: transparent; }
  .cover--ringed  { --panel: var(--brand-navy); --band: var(--brand-blue); --ring: var(--brand-blue); }

  .cover-one   { left: 28px; top: 40px;  width: 678px; height: 258px; }
  .cover-two   { left: 28px; top: 319px; width: 678px; height: 258px; }
  .cover-three { left: 28px; top: 599px; width: 678px; height: 258px; }
  .cover-four  { left: 214px; top: 919px; width: 402px; height: 152px; }

  .defs-holder { position: absolute; width: 0; height: 0; overflow: hidden; }
  .tagline   { font-weight: 500; font-size: 30px; fill: var(--white); }
  .web-link  { font-weight: 800; font-size: 26px; fill: var(--white); }
  .call-label{ font-weight: 400; font-size: 41px; fill: var(--white); }
  .phone     { font-weight: 800; font-size: 69px; fill: var(--white); }
  .brand-name{ font-weight: 500; font-size: 27px; fill: var(--brand-navy); }
</style>
</head>
<body>
<main class="sheet">

  <svg class="defs-holder" aria-hidden="true" focusable="false">
    <defs>
      <linearGradient id="swoosh-top" x1="0" y1="0" x2="1" y2="0">
        <stop offset="0" stop-color="#ec1f27"/>
        <stop offset="0.6" stop-color="#8a3a78"/>
        <stop offset="1" stop-color="#1f66ae" stop-opacity="0"/>
      </linearGradient>
      <linearGradient id="swoosh-low" x1="0" y1="0" x2="1" y2="0.3">
        <stop offset="0" stop-color="#1f66ae" stop-opacity="0"/>
        <stop offset="0.55" stop-color="#8a3a78"/>
        <stop offset="1" stop-color="#ec1f27"/>
      </linearGradient>
      <linearGradient id="swoosh-edge" x1="0" y1="0" x2="1" y2="0">
        <stop offset="0" stop-color="#1f66ae" stop-opacity="0"/>
        <stop offset="1" stop-color="#ec1f27"/>
      </linearGradient>
      <linearGradient id="photo-tone" x1="0" y1="0" x2="1" y2="0.4">
        <stop offset="0" stop-color="#e8cba5"/>
        <stop offset="0.45" stop-color="#d6a874"/>
        <stop offset="0.8" stop-color="#efe6dc"/>
        <stop offset="1" stop-color="#f7f4f0"/>
      </linearGradient>

      <symbol id="cover-art" viewBox="0 0 1392 530">
        <rect class="panel" width="1392" height="530" style="fill: var(--panel)"/>
        <path class="light-band" d="M0 460 L160 200 L330 200 L120 530 L0 530 Z" style="fill: var(--band)"/>
        <path class="swoosh" d="M470 0 H600 L560 240 C500 250 440 230 420 160 C405 100 440 40 470 0 Z" fill="url(#swoosh-top)"/>
        <path class="swoosh" d="M150 530 L240 290 C270 200 380 200 345 330 L250 530 Z" fill="url(#swoosh-low)"/>
        <path class="swoosh" d="M600 530 L720 350 L800 350 L800 530 Z" fill="url(#swoosh-edge)"/>

        <path class="white-field" d="M561 0 A335 335 0 0 0 764 530 H1392 V0 Z" fill="#ffffff"/>
        <path class="photo-frame" d="M593 0 A310 310 0 1 0 1110 333 L1300 0 Z"
              fill="url(#photo-tone)" style="stroke: var(--ring)" stroke-width="24"
              role="img" aria-label="Photo of a golden retriever with a puppy and a white shepherd running in snow"/>

        <text class="tagline" x="60" y="90">Lorem ipsum dolor sit amet,</text>
        <text class="tagline" x="60" y="134">consectetur adipiscing elit,</text>
        <text class="tagline" x="60" y="178">sed do eiusmod tempor</text>
        <text class="web-link" x="64" y="290">www.bramblehound.example</text>
        <text class="call-label" x="64" y="396">CALL NOW:</text>
        <text class="phone" x="62" y="472">318-557-0249</text>

        <rect class="brand-mark" x="1218" y="318" width="56" height="56" style="fill: var(--brand-navy)"/>
        <text class="brand-name" x="1246" y="418" text-anchor="middle">BRAMBLEHOUND</text>
      </symbol>
    </defs>
  </svg>

  <svg class="cover cover--classic cover-one" viewBox="0 0 1392 530" role="group" aria-label="Cover banner, blue version">
    <use href="#cover-art"/>
  </svg>
  <svg class="cover cover--navy cover-two" viewBox="0 0 1392 530" role="group" aria-label="Cover banner, navy version">
    <use href="#cover-art"/>
  </svg>
  <svg class="cover cover--ringed cover-three" viewBox="0 0 1392 530" role="group" aria-label="Cover banner, navy version with blue ring">
    <use href="#cover-art"/>
  </svg>
  <svg class="cover cover--classic cover-four" viewBox="0 0 1392 530" role="group" aria-label="Cover banner at page size">
    <use href="#cover-art"/>
  </svg>

</main>
</body>
</html>
```